6"x9" Postcard Mailer

A 6"x9" Postcard mailer targeted to forensic laboratories to advertise or mock forensic samples (https://veltrascience.example/products/trial-case-kits/).

Here is some copy, but we can modify if there is not enough space:

Headline:
Expedite Training, Validation, & R&D with Our Ready-to-Use Mock Samples

Bullet Points:

- Wide Variety of Sample Types: IRB-approved samples mimicking crime scene substances, including semen, hair, bone, saliva, blood, and vaginal epithelial cells.
- Diverse Scenarios: Simulate sexual assault and degraded samples for varied conditions.
- Custom Solutions: Tailored DNA quantities and concentrations to suit your lab's needs.

Use discount code TRAL58 for a 10% discount

```html
<!DOCTYPE html>
<html lang="en">
<head>
<meta charset="utf-8">
<title>Mock Samples Postcard Mailer</title>
<link href="https://fonts.googleapis.com/css2?family=Quicksand:wght@400;500;700&display=swap" rel="stylesheet">
<style>
  :root {
    --page-bg: #d9d9d9;
    --card-bg: #fbfbfb;
    --teal: #46b5b2;
    --teal-dark: #2f8c86;
    --yellow: #fbcf2d;
    --ink: #4a4a4a;
    --ink-dark: #333333;
  }
  html, body {
    margin: 0;
    width: 1200px;
    height: 800px;
    overflow: hidden;
    background: var(--page-bg);
    font-family: "Quicksand", sans-serif;
  }
  .postcard {
    position: absolute;
    left: 60px;
    top: 40px;
    width: 1080px;
    height: 720px;
    background: var(--card-bg);
    overflow: hidden;
    box-shadow: 0 18px 40px rgba(0,0,0,0.18);
  }
  .postcard-shapes,
  .hero-photo {
    position: absolute;
    left: 0;
    top: 0;
    width: 1080px;
    height: 720px;
  }
  .headline {
    position: absolute;
    left: 50px;
    top: 58px;
    width: 510px;
    margin: 0;
    color: var(--teal);
    font-weight: 700;
    font-size: 37px;
    line-height: 1.2;
  }
  .benefits {
    position: absolute;
    left: 50px;
    top: 232px;
    width: 440px;
    margin: 0;
    padding: 0;
    list-style: none;
    color: var(--ink);
    font-size: 20px;
    font-weight: 500;
    line-height: 1.3;
  }
  .benefits li {
    position: relative;
    padding-left: 18px;
    margin-bottom: 30px;
    text-align: justify;
    hyphens: auto;
  }
  .benefits li::before {
    content: "";
    position: absolute;
    left: 0;
    top: 10px;
    width: 8px;
    height: 8px;
    border-radius: 50%;
    background: var(--yellow);
  }
  .offer {
    position: absolute;
    right: 40px;
    top: 575px;
    text-align: right;
    color: var(--ink-dark);
  }
  .offer-lead {
    font-size: 30px;
    font-weight: 400;
    line-height: 1.1;
  }
  .offer-code {
    color: var(--teal);
    font-size: 36px;
    font-weight: 700;
    line-height: 1.1;
  }
  .offer-note {
    font-size: 23px;
    font-weight: 500;
    line-height: 1.3;
  }
  .offer-note strong { font-weight: 700; }
</style>
</head>
<body>
  <section class="postcard">
    <svg class="postcard-shapes" viewBox="0 0 1080 720" aria-hidden="true">
      <polygon class="band-teal" points="0,620 560,575 640,720 0,720" fill="var(--teal)"/>
      <polygon class="photo-frame" points="598,0 1080,0 1080,560 700,560 535,350" fill="var(--teal-dark)"/>
    </svg>

    <svg class="hero-photo" viewBox="0 0 1080 720" role="img" aria-label="Gloved hands swabbing a blood stain on a white surface at a crime scene">
      <defs>
        <linearGradient id="photoTone" x1="0" y1="0" x2="1" y2="1">
          <stop offset="0" stop-color="#3a3d42"/>
          <stop offset="0.35" stop-color="#5a73b8"/>
          <stop offset="0.6" stop-color="#c9ccd2"/>
          <stop offset="0.85" stop-color="#e8e6e8"/>
          <stop offset="1" stop-color="#d88a92"/>
        </linearGradient>
      </defs>
      <polygon points="618,0 1080,0 1080,560 712,560 553,350" fill="url(#photoTone)"/>
    </svg>

    <svg class="postcard-shapes" viewBox="0 0 1080 720" aria-hidden="true">
      <polygon class="offer-panel" points="680,560 1080,560 1080,720 760,720 640,640" fill="var(--yellow)"/>
    </svg>

    <h1 class="headline">Expedite Training, Validation, &amp; R&amp;D with Our Ready-to-Use Mock Samples</h1>

    <ul class="benefits">
      <li>Wide Variety of Sample Types: IRB-approved samples mimicking crime scene substances, including semen, hair, bone, saliva, blood, and vaginal epithelial cells.</li>
      <li>Diverse Scenarios: Simulate sexual assault and degraded samples for varied conditions.</li>
      <li>Custom Solutions: Tailored DNA quantities and concentrations to suit your lab's needs.</li>
    </ul>

    <div class="offer">
      <div class="offer-lead">Use discount code</div>
      <div class="offer-code">TRAL58</div>
      <div class="offer-note">or a <strong>10% discount</strong></div>
    </div>
  </section>
</body>
</html>
```